Tidewell Claimworks Website - a medical billing website - one page

I need a one-page website to attract potential clients to my medical billing services - I am in the process of creating a logo, the contest ends Friday. I also have some ideas and am writing some of the copy that I can send you.

SLOGAN: We Turn Codes Into Money

MISSION STATEMENT: Give compassionate quality service and precision medical billing with urgency

Target Market(s)

MD's, physical therapists, occupational therapists, speech therapists, chiropractors, psychologists, psychiatrists, dentists and new grads of the above

Coding

Coded - Design and coding required

Number of Pages Required

1 page

Font styles to use
Sans Serif
Decorative
Script

Colors
33a6d7
add136
87cfc6
cadf82
9bcb3c
85cae6

Requirements
Must have
• I am working on the major points of copy that I need, plus
• ranking search terms keywords and phrases
Nice to have
• creativity to draw clients in
• my color choices below are similar to the logo coloring - but if you like something different feel free to use your own creative colors.

```html
<!DOCTYPE html>
<html lang="en">
<head>
<meta charset="utf-8">
<title>Tidewell Claimworks — Medical Billing</title>
<link href="https://fonts.googleapis.com/css2?family=Poppins:wght@500;600;700;800&family=Roboto:ital,wght@0,400;0,500;0,700;1,400&display=swap" rel="stylesheet">
<style>
:root{
  --blue:#2f93d1;
  --green:#8dc63f;
  --ink:#1f1f1f;
  --text:#6b6b6b;
  --soft:#f7f7f7;
  --backdrop:#c7c7c7;
}
*{margin:0;padding:0;box-sizing:border-box}
html,body{width:1200px;height:2290px;overflow:hidden;background:var(--backdrop)}
body{font-family:Roboto,Arial,sans-serif;color:var(--text)}
.stage{position:absolute;left:0;top:0;width:1350px;height:2576px;transform:scale(.888889);transform-origin:0 0}
.page{position:absolute;top:72px;width:580px;height:2433px;background:#fff;overflow:hidden}
.page--main{left:63px}
.page--modal{left:707px}
.page *{position:absolute}
.page span,.page b,.page br{position:static}

/* header */
.site-header{left:0;top:0;width:580px;height:50px;background:#fff;border-top:3px solid var(--blue)}
.brand-dot{left:55px;top:11px;width:24px;height:24px;border-radius:50%;border:3px solid var(--blue)}
.brand-name{left:88px;top:16px;font:600 9.5px Poppins,sans-serif;color:var(--blue);white-space:nowrap}
.nav{left:238px;top:18px;display:flex;gap:12px;font:500 7px Roboto,sans-serif;color:var(--ink);white-space:nowrap}
.nav span{position:relative}
.nav .is-active{color:var(--green);border-bottom:1px solid var(--green);padding-bottom:5px}
.nav-search{left:520px;top:17px;width:9px;height:9px}

/* hero */
.hero{left:0;top:50px;width:580px;height:250px;background:
  radial-gradient(ellipse 140px 170px at 460px 110px,rgba(255,255,255,.75),rgba(255,255,255,0)),
  linear-gradient(180deg,rgba(0,0,0,0) 70%,rgba(60,60,70,.25) 100%),
  linear-gradient(100deg,#4a5890 0%,#7683b0 28%,#c6ccdc 50%,#ecebe8 68%,#d6d1ca 100%)}
.hero-title{left:53px;top:116px;font:800 20px Poppins,sans-serif;letter-spacing:.2px;white-space:nowrap}
.hero-title .t1{color:var(--blue)}
.hero-title .t2{color:var(--green)}
.hero-text{left:53px;top:153px;width:270px;font:400 8.2px/14px Roboto,sans-serif;color:#111}
.btn{border-radius:14px;background:var(--green);color:#fff;font:700 7.5px Roboto,sans-serif;text-align:center}
.hero-btn{left:53px;top:196px;width:100px;height:28px;line-height:28px}
.round-arrow{width:19px;height:19px;border-radius:50%;border:1px solid #fff}
.hero .prev,.hero .next{top:115px}
.hero .prev{left:16px}.hero .next{left:547px}

/* headings */
.h2{font:600 18px Poppins,sans-serif;color:var(--ink);white-space:nowrap}
.center{left:0;width:580px;text-align:center}
.para{font:400 6.6px/12px Roboto,sans-serif;color:var(--text)}

/* who */
.who-photo{left:54px;top:360px;width:203px;height:135px;border:3px solid #fff;box-shadow:0 1px 5px rgba(0,0,0,.25);background:
  radial-gradient(ellipse 50px 60px at 140px 75px,#3f6c9e,rgba(63,108,158,0)),
  linear-gradient(110deg,#cdc8c0 0%,#ecebe7 40%,#9fb3c8 70%,#d9dde1 100%)}
.who-title{left:289px;top:360px}
.who-text{left:289px;top:396px;width:238px;text-align:justify}
.billing-title{left:54px;top:550px}
.billing-text{left:55px;top:585px;width:470px}

/* tiles */
.tile{top:619px;width:145px;height:145px}
.tile--blue{background:radial-gradient(ellipse 90px 70px at 70% 30%,rgba(255,255,255,.22),rgba(255,255,255,0)),linear-gradient(160deg,#6fb4e3,#3d9bd8)}
.tile--green{background:radial-gradient(ellipse 90px 70px at 60% 30%,rgba(255,255,255,.2),rgba(255,255,255,0)),linear-gradient(160deg,#b7db5c,#a0cd37)}
.tile-icon{left:15px;top:86px;width:17px;height:20px}
.tile-label{left:15px;top:116px;font:500 8px Roboto,sans-serif;color:#fff;white-space:nowrap}

/* specialities */
.spec-title{top:822px}
.spec-text{top:856px;left:90px;width:400px;text-align:center}
.card{top:903px;width:147px;height:180px;background:#fff;box-shadow:0 1px 4px rgba(0,0,0,.14)}
.card-photo{left:0;top:0;width:147px;height:90px}
.card-icon{left:59px;top:76px;width:29px;height:29px;border-radius:50%;background:var(--blue);border:2px solid #fff}
.card-icon svg{position:absolute;left:6px;top:6px;width:13px;height:13px}
.card-name{left:0;top:112px;width:147px;text-align:center;font:500 8.2px Roboto,sans-serif;color:var(--ink)}
.card-text{left:10px;top:130px;width:127px;text-align:center;font:400 6.4px/12px Roboto,sans-serif}
.spec-arrow{top:983px;border:none}

/* benefits */
.benefits{left:0;top:1143px;width:580px;height:317px;background:var(--soft)}
.ben-title{top:1173px}
.ben-sub{top:1202px;text-align:center;left:0;width:580px}
.ben-lines{left:0;top:1143px;width:580px;height:317px}
.ben-item{width:130px}
.ben-item h4{position:static;font:500 7.5px/11px Roboto,sans-serif;color:var(--ink);margin-bottom:6px}
.ben-item p{position:static;font:400 6.4px/11px Roboto,sans-serif}
.ben-item--l{text-align:right}
.ben-icon{width:30px;height:30px;border-radius:50%;background:var(--green);border:3px solid #e1efc6}
.ben-icon svg{position:absolute;left:6px;top:6px;width:12px;height:12px}
.ben-core{left:254px;top:1250px;width:72px;height:72px;border-radius:50%;background:#fff;border:2px solid #dfe9f3;box-shadow:0 0 0 5px #fff}
.ben-core i{position:absolute;left:16px;top:16px;width:36px;height:36px;border-radius:50%;border:3px solid var(--blue)}

/* team */
.team-title{top:1516px}
.member{top:1562px;width:104px;height:141px;background:#f3f5f8;border:3px solid #dde3ea}
.member-photo{left:8px;top:6px;width:82px;height:82px;border-radius:50%;background:radial-gradient(circle at 50% 35%,#efe9e3 0%,#cfc9c2 45%,#7e838a 100%)}
.member-name{left:0;top:94px;width:98px;text-align:center;font:500 7px Roboto,sans-serif;color:var(--ink)}
.member-role{left:0;top:106px;width:98px;text-align:center;font:400 5.4px Roboto,sans-serif}
.member-city{left:0;top:120px;width:98px;text-align:center;font:700 5.4px Roboto,sans-serif;color:var(--ink)}

/* testimonials */
.testimonials{left:0;top:1764px;width:580px;height:147px;background:var(--green)}
.testi-title{top:1782px;color:#fff}
.testi-arrow{top:1829px;width:17px;height:17px;border-radius:50%;background:#fff}
.testi-avatar{left:114px;top:1814px;width:50px;height:50px;border-radius:50%;border:3px solid #fff;background:radial-gradient(circle at 50% 40%,#ead6c6 0%,#b9c6d6 55%,#4f78a6 100%)}
.quote-mark{font:800 20px Poppins,sans-serif;color:#fff;line-height:1}
.testi-text{left:197px;top:1822px;width:272px;font:italic 400 7px/11px Roboto,sans-serif;color:#fff}
.testi-name{left:197px;top:1866px;font:500 7.5px Roboto,sans-serif;color:#273a10}
.testi-co{left:197px;top:1877px;font:400 5.5px Roboto,sans-serif;color:#fff}

/* blog */
.blog-title{top:1960px}
.blog-feature{left:72px;top:2003px;width:211px;height:159px;background:radial-gradient(ellipse 60px 70px at 160px 50px,#f3e7d6,rgba(243,231,214,0)),linear-gradient(110deg,#c8d2dc,#eef1f4 50%,#e2dcd3)}
.blog-feature-box{left:127px;top:2085px;width:156px;height:77px;background:var(--blue);padding:8px 10px;color:#fff}
.blog-feature-box *{position:static;display:block}
.bf-title{font:400 7px/11px Roboto,sans-serif}
.bf-meta{font:italic 400 5.5px Roboto,sans-serif;margin:5px 0}
.bf-text{font:400 6px/9px Roboto,sans-serif}
.post-photo{left:297px;width:84px;height:74px}
.post{left:391px;width:128px}
.post *{position:static;display:block}
.post-title{font:500 7px Roboto,sans-serif;color:var(--ink)}
.post-meta{font:italic 400 5.5px Roboto,sans-serif;color:var(--green);margin:5px 0 7px}
.post-text{font:400 6px/9.5px Roboto,sans-serif}

/* footer */
.footer{left:0;top:2228px;width:580px;height:205px;background:var(--blue)}
.f-head{font:500 8px Roboto,sans-serif;color:#fff;top:2258px}
.field{height:18px;background:#fff;font:400 5.8px Roboto,sans-serif;color:#666;padding:6px 9px}
.f-submit{left:53px;top:2376px;width:47px;height:13px;line-height:13px;font-size:6px}
.f-links{left:311px;top:2278px;font:400 6.2px/14px Roboto,sans-serif;color:#fff}
.f-links *{position:static;display:block}
.f-contact{left:397px;top:2278px;width:140px;font:400 6.4px/11px Roboto,sans-serif;color:#fff}
.f-contact *{position:static;display:flex;gap:6px;margin-bottom:4px}
.f-contact svg{position:static;flex:none;margin-top:2px}
.stay{left:311px;top:2364px;font:500 7.4px Roboto,sans-serif;color:#fff}
.social{top:2361px;width:14px;height:14px;border-radius:50%;background:#fff}
.f-rule{left:53px;top:2398px;width:474px;height:1px;background:rgba(255,255,255,.35)}
.copy{top:2413px;font:400 6.2px Roboto,sans-serif;color:#fff}

/* modal state */
.dim{left:0;top:0;width:580px;height:2433px;background:rgba(30,30,30,.5)}
.popup{left:173px;top:118px;width:235px;height:153px;background:#fff}
.popup-close{left:226px;top:-5px;width:11px;height:11px}
.pop-dot{left:12px;top:13px;width:13px;height:13px;border-radius:50%;border:2px solid var(--blue)}
.pop-brand{left:32px;top:17px;font:600 5px Poppins,sans-serif;color:var(--blue)}
.pop-small{left:12px;top:45px;font:400 4.4px Roboto,sans-serif;color:#333}
.pop-head{left:12px;top:54px;font:700 10.5px Poppins,sans-serif;color:var(--blue)}
.pop-sub{left:12px;top:70px;font:400 4.8px Roboto,sans-serif;color:#333}
.pop-field{left:12px;top:86px;width:117px;height:17px;border:1px solid #ddd;background:#f4f4f4;font:400 5px Roboto,sans-serif;color:#666;padding:5px}
.pop-btn{left:12px;top:114px;width:68px;height:18px;line-height:18px;font-size:6px}
.pop-art{left:142px;top:32px;width:84px;height:100px;background:radial-gradient(ellipse 40px 50px at 55% 45%,#3d8fe0,rgba(61,143,224,0)),radial-gradient(ellipse 60px 60px at 50% 55%,#e8f2fc,#ffffff)}
</style>
</head>
<body>
<div class="stage">

<main class="page page--main">
  <header class="site-header">
    <i class="brand-dot"></i>
    <div class="brand-name">Tidewell Claimworks</div>
    <nav class="nav"><span class="is-active">Home</span><span>About us</span><span>Services</span><span>Speciality</span><span>Benefits</span><span>Blog</span><span>Contact Us</span></nav>
    <svg class="nav-search" viewBox="0 0 10 10"><circle cx="4" cy="4" r="3" fill="none" stroke="#222" stroke-width="1.4"/><path d="M6.3 6.3 9 9" stroke="#222" stroke-width="1.4"/></svg>
  </header>

  <section class="hero" role="img" aria-label="Doctor in a white coat working on a laptop at a desk">
    <svg class="round-arrow prev" viewBox="0 0 19 19"><path d="M11 5 7 9.5 11 14" fill="none" stroke="#fff" stroke-width="1.3"/></svg>
    <svg class="round-arrow next" viewBox="0 0 19 19"><path d="M8 5l4 4.5L8 14" fill="none" stroke="#fff" stroke-width="1.3"/></svg>
  </section>
  <h1 class="hero-title"><span class="t1">TIDEWELL </span><span class="t2">CLAIMWORKS</span></h1>
  <p class="hero-text">Lorem ipsum dolor sit amet, consectetur adipiscing elit, sed do tempor incididunt ut labore et dolore magna aliqua.</p>
  <div class="btn hero-btn">CONTACT US &#10140;</div>

  <div class="who-photo" role="img" aria-label="Nurse reviewing a tablet with a patient"></div>
  <h2 class="h2 who-title">Who We Are</h2>
  <p class="para who-text">Sed ut perspiciatis unde omnis iste natus accusantium doloremque laudantium, totam rem aperiam, eaque ipsa quae ab inventore veritatis et quasi architecto beatae vitae dicta sunt explicabo. Nemo enim ipsam voluptatem quia voluptas sit aspernatur aut odit aut fugit, sed quia consequuntur magni dolores eos ratione voluptatem sequi nesciunt. Neque porro quisquam est, qui dolorem ipsum quia dolor sit amet, consectetur, adipisci velit, sed quia non numquam</p>

  <h2 class="h2 billing-title">Billing Services</h2>
  <p class="para billing-text">Sed ut perspiciatis unde omnis iste natus error sit voluptatem accusantium doloremque laudantium totam rem aperiam.</p>

  <div class="tile tile--blue" style="left:0" role="img" aria-label="Hands signing an insurance form, tinted blue"><svg class="tile-icon" viewBox="0 0 17 20"><rect x="1" y="1" width="15" height="18" rx="1" fill="none" stroke="#fff"/><path d="M4 6h9M4 10h9M4 14h6" stroke="#fff"/></svg><div class="tile-label">Patient Insurance Verification</div></div>
  <div class="tile tile--green" style="left:145px" role="img" aria-label="Medical team at work, tinted green"><svg class="tile-icon" viewBox="0 0 17 20"><rect x="1" y="1" width="15" height="18" rx="1" fill="none" stroke="#fff"/><path d="M4 6h9M4 10h9M4 14h6" stroke="#fff"/></svg><div class="tile-label">Medical Coding</div></div>
  <div class="tile tile--blue" style="left:290px" role="img" aria-label="Woman checking claims on a computer, tinted blue"><svg class="tile-icon" viewBox="0 0 17 20"><rect x="1" y="1" width="15" height="18" rx="1" fill="none" stroke="#fff"/><path d="M5 10l3 3 5-6" fill="none" stroke="#fff"/></svg><div class="tile-label">Claim Tracking</div></div>
  <div class="tile tile--green" style="left:435px" role="img" aria-label="Charts and a calculator on a desk, tinted green"><svg class="tile-icon" viewBox="0 0 17 20"><rect x="1" y="1" width="15" height="18" rx="1" fill="none" stroke="#fff"/><path d="M5 15V11M8.5 15V8M12 15V5" stroke="#fff"/></svg><div class="tile-label">Billing Analytics &amp; Reports</div></div>

  <h2 class="h2 center spec-title">We Are Specializing In</h2>
  <p class="para spec-text">Sed ut perspiciatis unde omnis iste natus error sit voluptatem accusantium doloremque laudantium, totam rem aperiam, eaque ipsa quae ab illo inventore veritatis et quasi architecto beatae vitae dicta sunt explicabo.</p>
  <svg class="round-arrow spec-arrow" style="left:16px" viewBox="0 0 19 19"><circle cx="9.5" cy="9.5" r="9" fill="#fff" stroke="#2f93d1"/><path d="M11 5 7 9.5 11 14" fill="none" stroke="#2f93d1" stroke-width="1.3"/></svg>
  <svg class="round-arrow spec-arrow" style="left:547px" viewBox="0 0 19 19"><circle cx="9.5" cy="9.5" r="9" fill="#fff" stroke="#2f93d1"/><path d="M8 5l4 4.5L8 14" fill="none" stroke="#2f93d1" stroke-width="1.3"/></svg>
  <article class="card" style="left:54px"><div class="card-photo" role="img" aria-label="Therapist with an older patient" style="background:radial-gradient(ellipse 40px 35px at 35% 60%,#6f8fbf,rgba(111,143,191,0)),linear-gradient(120deg,#e4e6e9,#c9ccd1 60%,#8e96a3)"></div><i class="card-icon"><svg viewBox="0 0 13 13"><path d="M6.5 2v9M2 6.5h9" stroke="#fff" stroke-width="2"/></svg></i><h3 class="card-name">Physical Therapists</h3><p class="card-text">At vero eos et accusamus et iusto odio dignissimos qui blanditiis praesentium voluptatum deleniti atque corrupti</p></article>
  <article class="card" style="left:217px"><div class="card-photo" role="img" aria-label="Therapist talking with a child" style="background:radial-gradient(ellipse 40px 40px at 65% 60%,#3b3e45,rgba(59,62,69,0)),linear-gradient(120deg,#ecebe8,#c8c6c2 55%,#8d8f95)"></div><i class="card-icon"><svg viewBox="0 0 13 13"><circle cx="6.5" cy="4" r="2.2" fill="none" stroke="#fff" stroke-width="1.4"/><path d="M2.5 12a4 4 0 0 1 8 0" fill="none" stroke="#fff" stroke-width="1.4"/></svg></i><h3 class="card-name">Speech Therapists</h3><p class="card-text">At vero eos et accusamus et iusto odio dignissimos qui blanditiis praesentium voluptatum deleniti atque corrupti</p></article>
  <article class="card" style="left:380px"><div class="card-photo" role="img" aria-label="Psychologist seated in an office" style="background:radial-gradient(ellipse 30px 40px at 30% 45%,#ffffff,rgba(255,255,255,0)),linear-gradient(120deg,#f1eee9,#ddd6cc 55%,#b6ab9c)"></div><i class="card-icon"><svg viewBox="0 0 13 13"><circle cx="6.5" cy="6.5" r="4.5" fill="none" stroke="#fff" stroke-width="1.4"/><path d="M4.5 6.5h4M6.5 4.5v4" stroke="#fff" stroke-width="1.3"/></svg></i><h3 class="card-name">Psychologists</h3><p class="card-text">At vero eos et accusamus et iusto odio dignissimos qui blanditiis praesentium voluptatum deleniti atque corrupti</p></article>

  <section class="benefits"></section>
  <svg class="ben-lines" viewBox="0 0 580 317"><g stroke="#d6d6d6" fill="none"><path d="M202 110H235L290 143 345 110H377M202 194H235L290 143 345 194H377M290 143V234"/></g></svg>
  <h2 class="h2 center ben-title">Our Benefits</h2>
  <p class="para ben-sub">Lorem ipsum dolor sit amet, consectetur adipiscing elit, sed do eiusmod tempor</p>
  <div class="ben-core"><i></i></div>
  <div class="ben-icon" style="left:187px;top:1238px"><svg viewBox="0 0 12 12"><rect x="2" y="1" width="8" height="10" rx="1" fill="none" stroke="#fff"/><path d="M4 4h4M4 6h4M4 8h2.5" stroke="#fff"/></svg></div>
  <div class="ben-icon" style="left:362px;top:1238px"><svg viewBox="0 0 12 12"><rect x="1" y="2" width="10" height="8" rx="1" fill="none" stroke="#fff"/><path d="M3 8V6M5 8V4.5M7 8V5.5M9 8V4" stroke="#fff"/></svg></div>
  <div class="ben-icon" style="left:187px;top:1322px"><svg viewBox="0 0 12 12"><rect x="2.5" y="5" width="7" height="6" rx="1" fill="none" stroke="#fff"/><path d="M4 5V3.5a2 2 0 0 1 4 0V5" fill="none" stroke="#fff"/></svg></div>
  <div class="ben-icon" style="left:362px;top:1322px"><svg viewBox="0 0 12 12"><circle cx="6" cy="6" r="4.5" fill="none" stroke="#fff"/><path d="M6 3.5V6l2 1.3" fill="none" stroke="#fff"/></svg></div>
  <div class="ben-icon" style="left:275px;top:1362px"><svg viewBox="0 0 12 12"><path d="M2 10 5 6.5 7 8.5 10 3M7.5 3H10v2.5" fill="none" stroke="#fff"/></svg></div>
  <div class="ben-item ben-item--l" style="left:39px;top:1236px"><h4>Simplifying financial<br>record-keeping</h4><p>Sed perspiciatis unde omnis natus sit voluptatem accusantium</p></div>
  <div class="ben-item" style="left:411px;top:1236px"><h4>High accuracy</h4><p>Sed perspiciatis unde omnis natus accusantium laudantium, totam rem aperiam, eaque</p></div>
  <div class="ben-item ben-item--l" style="left:39px;top:1323px"><h4>Data protection for<br>sensitive files</h4><p>Sed perspiciatis unde omnis natus sit voluptatem accusantium</p></div>
  <div class="ben-item" style="left:411px;top:1323px"><h4>Quick turnaround time for<br>insurance claims</h4><p>Sed perspiciatis unde omnis natus sit voluptatem accusantium</p></div>
  <div class="ben-item" style="left:225px;top:1402px;text-align:center"><h4>Scalability</h4><p>Sed ut perspiciatis unde omnis</p></div>

  <h2 class="h2 center team-title">Our Team</h2>
  <div class="member" style="left:54px"><div class="member-photo" role="img" aria-label="Portrait of team member"></div><div class="member-name">MARA QUILL</div><div class="member-role">Founder And CEO</div><div class="member-city">SAN DIEGO, CA</div></div>
  <div class="member" style="left:177px"><div class="member-photo" role="img" aria-label="Portrait of team member"></div><div class="member-name">OWEN TARRANT</div><div class="member-role">Project Manager</div><div class="member-city">SAN DIEGO, CA</div></div>
  <div class="member" style="left:300px"><div class="member-photo" role="img" aria-label="Portrait of team member"></div><div class="member-name">FELIX BRANDT</div><div class="member-role">Founder And CEO</div><div class="member-city">SAN DIEGO, CA</div></div>
  <div class="member" style="left:423px"><div class="member-photo" role="img" aria-label="Portrait of team member"></div><div class="member-name">IRIS CALLOWAY</div><div class="member-role">Project Manager</div><div class="member-city">SAN DIEGO, CA</div></div>

  <section class="testimonials"></section>
  <h2 class="h2 center testi-title">Testimonials</h2>
  <svg class="testi-arrow" style="left:54px" viewBox="0 0 17 17"><path d="M12 8.5H5m3-3-3 3 3 3" fill="none" stroke="#222" stroke-width="1.3"/></svg>
  <svg class="testi-arrow" style="left:508px" viewBox="0 0 17 17"><path d="M5 8.5h7m-3-3 3 3-3 3" fill="none" stroke="#222" stroke-width="1.3"/></svg>
  <div class="testi-avatar" role="img" aria-label="Client portrait"></div>
  <div class="quote-mark" style="left:172px;top:1806px">&ldquo;</div>
  <p class="testi-text">Lorem ipsum dolor sit amet, consectetur adipiscing elit, sed do eiusmod tempor incididunt ut labore et dolore magna aliqua. Ut enim ad minim veniam, quis nostrud exercitation ullamco laboris nisi ut aliquip ex ea commodo consequat.</p>
  <div class="quote-mark" style="left:434px;top:1846px">&rdquo;</div>
  <div class="testi-name">John Doe</div>
  <div class="testi-co">Company Name</div>

  <h2 class="h2 center blog-title">Our Blog</h2>
  <div class="blog-feature" role="img" aria-label="Smiling doctor with a stethoscope"></div>
  <div class="blog-feature-box"><span class="bf-title">Lorem ipsum dolor amet, adipiscing elit, sed do eiusmod</span><span class="bf-meta">Jan 18,2020 &nbsp;|&nbsp; 2 Comments</span><span class="bf-text">Sed ut perspiciatis unde omnis iste natus error sit voluptatem accusantium</span></div>
  <div class="post-photo" style="top:2005px;background:linear-gradient(160deg,#eef0f2 0%,#c9d0d8 50%,#3e4650 100%)" role="img" aria-label="Billing documents beside a laptop"></div>
  <div class="post" style="top:2009px"><span class="post-title">Lorem ipsum dolor &nbsp;adipiscing</span><span class="post-meta">Jan 08,2020 &nbsp;|&nbsp; 2 Comments</span><span class="post-text">Sed ut perspiciatis unde omnis iste natus sit accusantium doloremque laudantium, totam rem</span></div>
  <div class="post-photo" style="top:2089px;background:linear-gradient(120deg,#dcdfe3 0%,#f1f1ef 50%,#9aa2ab 100%)" role="img" aria-label="Woman reading paperwork at a desk"></div>
  <div class="post" style="top:2093px"><span class="post-title">Lorem ipsum dolor &nbsp;adipiscing</span><span class="post-meta">Dec 25,2019 &nbsp;|&nbsp; 2 Comments</span><span class="post-text">Sed ut perspiciatis unde omnis iste natus sit accusantium doloremque laudantium, totam rem</span></div>

  <footer class="footer"></footer>
  <div class="f-head" style="left:53px">GET IN TOUCH</div>
  <div class="field" style="left:53px;top:2272px;width:114px">First Name</div>
  <div class="field" style="left:171px;top:2272px;width:114px">Last Name</div>
  <div class="field" style="left:53px;top:2296px;width:114px">Email</div>
  <div class="field" style="left:171px;top:2296px;width:114px">phone number</div>
  <div class="field" style="left:53px;top:2319px;width:232px;height:36px">Message</div>
  <div class="btn f-submit">SUBMIT</div>
  <div class="f-head" style="left:311px">QUICK LINKS</div>
  <div class="f-links"><span>&raquo;&nbsp; Home</span><span>&raquo;&nbsp; About us</span><span>&raquo;&nbsp; Services</span><span>&raquo;&nbsp; Speciality</span><span>&raquo;&nbsp; Contact Us</span></div>
  <div class="f-head" style="left:397px">CONTACT US</div>
  <div class="f-contact">
    <span><svg width="6" height="8" viewBox="0 0 6 8"><path d="M3 8S0 4.5 0 3a3 3 0 0 1 6 0C6 4.5 3 8 3 8z" fill="#fff"/></svg>123, Lorem ipsum dolor sit amet, consectetur elit, sed</span>
    <span><svg width="6" height="8" viewBox="0 0 6 8"><rect x="1" width="4" height="8" rx="1" fill="#fff"/></svg>(123) 555-0142</span>
    <span><svg width="6" height="8" viewBox="0 0 6 8"><rect width="6" height="7" rx="1" fill="#fff"/></svg>+888 555 0188</span>
    <span><svg width="7" height="6" viewBox="0 0 7 6"><rect x=".5" y=".5" width="6" height="5" fill="none" stroke="#fff"/><path d="M.5.5 3.5 3 6.5.5" fill="none" stroke="#fff"/></svg>info@tidewellclaimworks.com</span>
  </div>
  <div class="stay">STAY CONNECTED :</div>
  <i class="social" style="left:409px"></i><i class="social" style="left:427px"></i><i class="social" style="left:445px"></i>
  <div class="f-rule"></div>
  <div class="copy center">© 2020 Tidewell Claimworks. &nbsp;| All Rights Reserved | Terms and Conditions</div>
</main>

<main class="page page--modal">
  <header class="site-header">
    <i class="brand-dot"></i>
    <div class="brand-name">Tidewell Claimworks</div>
    <nav class="nav"><span class="is-active">Home</span><span>About us</span><span>Services</span><span>Speciality</span><span>Benefits</span><span>Blog</span><span>Contact Us</span></nav>
    <svg class="nav-search" viewBox="0 0 10 10"><circle cx="4" cy="4" r="3" fill="none" stroke="#222" stroke-width="1.4"/><path d="M6.3 6.3 9 9" stroke="#222" stroke-width="1.4"/></svg>
  </header>

  <section class="hero" role="img" aria-label="Doctor in a white coat working on a laptop at a desk">
    <svg class="round-arrow prev" viewBox="0 0 19 19"><path d="M11 5 7 9.5 11 14" fill="none" stroke="#fff" stroke-width="1.3"/></svg>
    <svg class="round-arrow next" viewBox="0 0 19 19"><path d="M8 5l4 4.5L8 14" fill="none" stroke="#fff" stroke-width="1.3"/></svg>
  </section>
  <h1 class="hero-title"><span class="t1">TIDEWELL </span><span class="t2">CLAIMWORKS</span></h1>
  <p class="hero-text">Lorem ipsum dolor sit amet, consectetur adipiscing elit, sed do tempor incididunt ut labore et dolore magna aliqua.</p>
  <div class="btn hero-btn">CONTACT US &#10140;</div>

  <div class="who-photo" role="img" aria-label="Nurse reviewing a tablet with a patient"></div>
  <h2 class="h2 who-title">Who We Are</h2>
  <p class="para who-text">Sed ut perspiciatis unde omnis iste natus accusantium doloremque laudantium, totam rem aperiam, eaque ipsa quae ab inventore veritatis et quasi architecto beatae vitae dicta sunt explicabo. Nemo enim ipsam voluptatem quia voluptas sit aspernatur aut odit aut fugit, sed quia consequuntur magni dolores eos ratione voluptatem sequi nesciunt. Neque porro quisquam est, qui dolorem ipsum quia dolor sit amet, consectetur, adipisci velit, sed quia non numquam</p>

  <h2 class="h2 billing-title">Billing Services</h2>
  <p class="para billing-text">Sed ut perspiciatis unde omnis iste natus error sit voluptatem accusantium doloremque laudantium totam rem aperiam.</p>

  <div class="tile tile--blue" style="left:0" role="img" aria-label="Hands signing an insurance form, tinted blue"><svg class="tile-icon" viewBox="0 0 17 20"><rect x="1" y="1" width="15" height="18" rx="1" fill="none" stroke="#fff"/><path d="M4 6h9M4 10h9M4 14h6" stroke="#fff"/></svg><div class="tile-label">Patient Insurance Verification</div></div>
  <div class="tile tile--green" style="left:145px" role="img" aria-label="Medical team at work, tinted green"><svg class="tile-icon" viewBox="0 0 17 20"><rect x="1" y="1" width="15" height="18" rx="1" fill="none" stroke="#fff"/><path d="M4 6h9M4 10h9M4 14h6" stroke="#fff"/></svg><div class="tile-label">Medical Coding</div></div>
  <div class="tile tile--blue" style="left:290px" role="img" aria-label="Woman checking claims on a computer, tinted blue"><svg class="tile-icon" viewBox="0 0 17 20"><rect x="1" y="1" width="15" height="18" rx="1" fill="none" stroke="#fff"/><path d="M5 10l3 3 5-6" fill="none" stroke="#fff"/></svg><div class="tile-label">Claim Tracking</div></div>
  <div class="tile tile--green" style="left:435px" role="img" aria-label="Charts and a calculator on a desk, tinted green"><svg class="tile-icon" viewBox="0 0 17 20"><rect x="1" y="1" width="15" height="18" rx="1" fill="none" stroke="#fff"/><path d="M5 15V11M8.5 15V8M12 15V5" stroke="#fff"/></svg><div class="tile-label">Billing Analytics &amp; Reports</div></div>

  <h2 class="h2 center spec-title">We Are Specializing In</h2>
  <p class="para spec-text">Sed ut perspiciatis unde omnis iste natus error sit voluptatem accusantium doloremque laudantium, totam rem aperiam, eaque ipsa quae ab illo inventore veritatis et quasi architecto beatae vitae dicta sunt explicabo.</p>
  <svg class="round-arrow spec-arrow" style="left:16px" viewBox="0 0 19 19"><circle cx="9.5" cy="9.5" r="9" fill="#fff" stroke="#2f93d1"/><path d="M11 5 7 9.5 11 14" fill="none" stroke="#2f93d1" stroke-width="1.3"/></svg>
  <svg class="round-arrow spec-arrow" style="left:547px" viewBox="0 0 19 19"><circle cx="9.5" cy="9.5" r="9" fill="#fff" stroke="#2f93d1"/><path d="M8 5l4 4.5L8 14" fill="none" stroke="#2f93d1" stroke-width="1.3"/></svg>
  <article class="card" style="left:54px"><div class="card-photo" role="img" aria-label="Therapist with an older patient" style="background:radial-gradient(ellipse 40px 35px at 35% 60%,#6f8fbf,rgba(111,143,191,0)),linear-gradient(120deg,#e4e6e9,#c9ccd1 60%,#8e96a3)"></div><i class="card-icon"><svg viewBox="0 0 13 13"><path d="M6.5 2v9M2 6.5h9" stroke="#fff" stroke-width="2"/></svg></i><h3 class="card-name">Physical Therapists</h3><p class="card-text">At vero eos et accusamus et iusto odio dignissimos qui blanditiis praesentium voluptatum deleniti atque corrupti</p></article>
  <article class="card" style="left:217px"><div class="card-photo" role="img" aria-label="Therapist talking with a child" style="background:radial-gradient(ellipse 40px 40px at 65% 60%,#3b3e45,rgba(59,62,69,0)),linear-gradient(120deg,#ecebe8,#c8c6c2 55%,#8d8f95)"></div><i class="card-icon"><svg viewBox="0 0 13 13"><circle cx="6.5" cy="4" r="2.2" fill="none" stroke="#fff" stroke-width="1.4"/><path d="M2.5 12a4 4 0 0 1 8 0" fill="none" stroke="#fff" stroke-width="1.4"/></svg></i><h3 class="card-name">Speech Therapists</h3><p class="card-text">At vero eos et accusamus et iusto odio dignissimos qui blanditiis praesentium voluptatum deleniti atque corrupti</p></article>
  <article class="card" style="left:380px"><div class="card-photo" role="img" aria-label="Psychologist seated in an office" style="background:radial-gradient(ellipse 30px 40px at 30% 45%,#ffffff,rgba(255,255,255,0)),linear-gradient(120deg,#f1eee9,#ddd6cc 55%,#b6ab9c)"></div><i class="card-icon"><svg viewBox="0 0 13 13"><circle cx="6.5" cy="6.5" r="4.5" fill="none" stroke="#fff" stroke-width="1.4"/><path d="M4.5 6.5h4M6.5 4.5v4" stroke="#fff" stroke-width="1.3"/></svg></i><h3 class="card-name">Psychologists</h3><p class="card-text">At vero eos et accusamus et iusto odio dignissimos qui blanditiis praesentium voluptatum deleniti atque corrupti</p></article>

  <section class="benefits"></section>
  <svg class="ben-lines" viewBox="0 0 580 317"><g stroke="#d6d6d6" fill="none"><path d="M202 110H235L290 143 345 110H377M202 194H235L290 143 345 194H377M290 143V234"/></g></svg>
  <h2 class="h2 center ben-title">Our Benefits</h2>
  <p class="para ben-sub">Lorem ipsum dolor sit amet, consectetur adipiscing elit, sed do eiusmod tempor</p>
  <div class="ben-core"><i></i></div>
  <div class="ben-icon" style="left:187px;top:1238px"><svg viewBox="0 0 12 12"><rect x="2" y="1" width="8" height="10" rx="1" fill="none" stroke="#fff"/><path d="M4 4h4M4 6h4M4 8h2.5" stroke="#fff"/></svg></div>
  <div class="ben-icon" style="left:362px;top:1238px"><svg viewBox="0 0 12 12"><rect x="1" y="2" width="10" height="8" rx="1" fill="none" stroke="#fff"/><path d="M3 8V6M5 8V4.5M7 8V5.5M9 8V4" stroke="#fff"/></svg></div>
  <div class="ben-icon" style="left:187px;top:1322px"><svg viewBox="0 0 12 12"><rect x="2.5" y="5" width="7" height="6" rx="1" fill="none" stroke="#fff"/><path d="M4 5V3.5a2 2 0 0 1 4 0V5" fill="none" stroke="#fff"/></svg></div>
  <div class="ben-icon" style="left:362px;top:1322px"><svg viewBox="0 0 12 12"><circle cx="6" cy="6" r="4.5" fill="none" stroke="#fff"/><path d="M6 3.5V6l2 1.3" fill="none" stroke="#fff"/></svg></div>
  <div class="ben-icon" style="left:275px;top:1362px"><svg viewBox="0 0 12 12"><path d="M2 10 5 6.5 7 8.5 10 3M7.5 3H10v2.5" fill="none" stroke="#fff"/></svg></div>
  <div class="ben-item ben-item--l" style="left:39px;top:1236px"><h4>Simplifying financial<br>record-keeping</h4><p>Sed perspiciatis unde omnis natus sit voluptatem accusantium</p></div>
  <div class="ben-item" style="left:411px;top:1236px"><h4>High accuracy</h4><p>Sed perspiciatis unde omnis natus accusantium laudantium, totam rem aperiam, eaque</p></div>
  <div class="ben-item ben-item--l" style="left:39px;top:1323px"><h4>Data protection for<br>sensitive files</h4><p>Sed perspiciatis unde omnis natus sit voluptatem accusantium</p></div>
  <div class="ben-item" style="left:411px;top:1323px"><h4>Quick turnaround time for<br>insurance claims</h4><p>Sed perspiciatis unde omnis natus sit voluptatem accusantium</p></div>
  <div class="ben-item" style="left:225px;top:1402px;text-align:center"><h4>Scalability</h4><p>Sed ut perspiciatis unde omnis</p></div>

  <h2 class="h2 center team-title">Our Team</h2>
  <div class="member" style="left:54px"><div class="member-photo" role="img" aria-label="Portrait of team member"></div><div class="member-name">MARA QUILL</div><div class="member-role">Founder And CEO</div><div class="member-city">SAN DIEGO, CA</div></div>
  <div class="member" style="left:177px"><div class="member-photo" role="img" aria-label="Portrait of team member"></div><div class="member-name">OWEN TARRANT</div><div class="member-role">Project Manager</div><div class="member-city">SAN DIEGO, CA</div></div>
  <div class="member" style="left:300px"><div class="member-photo" role="img" aria-label="Portrait of team member"></div><div class="member-name">FELIX BRANDT</div><div class="member-role">Founder And CEO</div><div class="member-city">SAN DIEGO, CA</div></div>
  <div class="member" style="left:423px"><div class="member-photo" role="img" aria-label="Portrait of team member"></div><div class="member-name">IRIS CALLOWAY</div><div class="member-role">Project Manager</div><div class="member-city">SAN DIEGO, CA</div></div>

  <section class="testimonials"></section>
  <h2 class="h2 center testi-title">Testimonials</h2>
  <svg class="testi-arrow" style="left:54px" viewBox="0 0 17 17"><path d="M12 8.5H5m3-3-3 3 3 3" fill="none" stroke="#222" stroke-width="1.3"/></svg>
  <svg class="testi-arrow" style="left:508px" viewBox="0 0 17 17"><path d="M5 8.5h7m-3-3 3 3-3 3" fill="none" stroke="#222" stroke-width="1.3"/></svg>
  <div class="testi-avatar" role="img" aria-label="Client portrait"></div>
  <div class="quote-mark" style="left:172px;top:1806px">&ldquo;</div>
  <p class="testi-text">Lorem ipsum dolor sit amet, consectetur adipiscing elit, sed do eiusmod tempor incididunt ut labore et dolore magna aliqua. Ut enim ad minim veniam, quis nostrud exercitation ullamco laboris nisi ut aliquip ex ea commodo consequat.</p>
  <div class="quote-mark" style="left:434px;top:1846px">&rdquo;</div>
  <div class="testi-name">John Doe</div>
  <div class="testi-co">Company Name</div>

  <h2 class="h2 center blog-title">Our Blog</h2>
  <div class="blog-feature" role="img" aria-label="Smiling doctor with a stethoscope"></div>
  <div class="blog-feature-box"><span class="bf-title">Lorem ipsum dolor amet, adipiscing elit, sed do eiusmod</span><span class="bf-meta">Jan 18,2020 &nbsp;|&nbsp; 2 Comments</span><span class="bf-text">Sed ut perspiciatis unde omnis iste natus error sit voluptatem accusantium</span></div>
  <div class="post-photo" style="top:2005px;background:linear-gradient(160deg,#eef0f2 0%,#c9d0d8 50%,#3e4650 100%)" role="img" aria-label="Billing documents beside a laptop"></div>
  <div class="post" style="top:2009px"><span class="post-title">Lorem ipsum dolor &nbsp;adipiscing</span><span class="post-meta">Jan 08,2020 &nbsp;|&nbsp; 2 Comments</span><span class="post-text">Sed ut perspiciatis unde omnis iste natus sit accusantium doloremque laudantium, totam rem</span></div>
  <div class="post-photo" style="top:2089px;background:linear-gradient(120deg,#dcdfe3 0%,#f1f1ef 50%,#9aa2ab 100%)" role="img" aria-label="Woman reading paperwork at a desk"></div>
  <div class="post" style="top:2093px"><span class="post-title">Lorem ipsum dolor &nbsp;adipiscing</span><span class="post-meta">Dec 25,2019 &nbsp;|&nbsp; 2 Comments</span><span class="post-text">Sed ut perspiciatis unde omnis iste natus sit accusantium doloremque laudantium, totam rem</span></div>

  <footer class="footer"></footer>
  <div class="f-head" style="left:53px">GET IN TOUCH</div>
  <div class="field" style="left:53px;top:2272px;width:114px">First Name</div>
  <div class="field" style="left:171px;top:2272px;width:114px">Last Name</div>
  <div class="field" style="left:53px;top:2296px;width:114px">Email</div>
  <div class="field" style="left:171px;top:2296px;width:114px">phone number</div>
  <div class="field" style="left:53px;top:2319px;width:232px;height:36px">Message</div>
  <div class="btn f-submit">SUBMIT</div>
  <div class="f-head" style="left:311px">QUICK LINKS</div>
  <div class="f-links"><span>&raquo;&nbsp; Home</span><span>&raquo;&nbsp; About us</span><span>&raquo;&nbsp; Services</span><span>&raquo;&nbsp; Speciality</span><span>&raquo;&nbsp; Contact Us</span></div>
  <div class="f-head" style="left:397px">CONTACT US</div>
  <div class="f-contact">
    <span><svg width="6" height="8" viewBox="0 0 6 8"><path d="M3 8S0 4.5 0 3a3 3 0 0 1 6 0C6 4.5 3 8 3 8z" fill="#fff"/></svg>123, Lorem ipsum dolor sit amet, consectetur elit, sed</span>
    <span><svg width="6" height="8" viewBox="0 0 6 8"><rect x="1" width="4" height="8" rx="1" fill="#fff"/></svg>(123) 555-0142</span>
    <span><svg width="6" height="8" viewBox="0 0 6 8"><rect width="6" height="7" rx="1" fill="#fff"/></svg>+888 555 0188</span>
    <span><svg width="7" height="6" viewBox="0 0 7 6"><rect x=".5" y=".5" width="6" height="5" fill="none" stroke="#fff"/><path d="M.5.5 3.5 3 6.5.5" fill="none" stroke="#fff"/></svg>info@tidewellclaimworks.com</span>
  </div>
  <div class="stay">STAY CONNECTED :</div>
  <i class="social" style="left:409px"></i><i class="social" style="left:427px"></i><i class="social" style="left:445px"></i>
  <div class="f-rule"></div>
  <div class="copy center">© 2020 Tidewell Claimworks. &nbsp;| All Rights Reserved | Terms and Conditions</div>

  <div class="dim"></div>
  <aside class="popup">
    <svg class="popup-close" viewBox="0 0 11 11"><circle cx="5.5" cy="5.5" r="5.5" fill="#111"/><path d="M3.5 3.5l4 4m0-4-4 4" stroke="#fff" stroke-width="1.1"/></svg>
    <i class="pop-dot"></i>
    <div class="pop-brand">Tidewell Claimworks</div>
    <div class="pop-small">Enter Your Email Address To</div>
    <div class="pop-head">Get your 1st 30 days</div>
    <div class="pop-sub">of billing for FREE – no obligations</div>
    <div class="pop-field">Your Email Address</div>
    <div class="btn pop-btn">SUBMIT</div>
    <div class="pop-art" role="img" aria-label="Isometric illustration of a phone with billing and payment icons"></div>
  </aside>
</main>

</div>
</body>
</html>
```